BrimDesk Virtual Assistant Flyer

I need a two sided, half page flyer, for my business BrimDesk. A company description is attached in the brief. The first side needs to be mostly eye catching and witty and the other side needs to be mostly informative. I want to make sure that the eye catching side also needs to let people know that BrimDesk is a virtual assistant. If this flyer were sitting on a table with 50 other fliers, I want this one to really pop and stand out. I want it to be professional but fun. Use the exact colors from logo please.
Updates

Target Market(s)

business professionals and entrepreneurs

Industry/Entity Type

Business

Requirements
Must have
• logo
Should not have
• All of the services listed. It makes the flyer too busy

```html
<!DOCTYPE html>
<html lang="en">
<head>
<meta charset="utf-8">
<title>BrimDesk Virtual Assistant Flyer</title>
<link rel="stylesheet" href="https://fonts.googleapis.com/css2?family=Montserrat:wght@400;600;700;800&display=swap">
<style>
  :root{
    --red:#c9402c;
    --green:#7dc242;
    --green-band:#8cc63f;
    --teal:#339ba5;
    --ink:#231f20;
    --paper:#ffffff;
    --mist:#eeeff0;
    --photo-cool:#c9d6de;
    --photo-warm:#d9cfc6;
  }
  *{margin:0;padding:0;box-sizing:border-box}
  html,body{width:1200px;height:1200px;overflow:hidden;background:var(--paper)}
  body{font-family:"Montserrat",Arial,sans-serif;color:var(--ink)}
  .stage{position:relative;width:1400px;height:1400px;transform:scale(.857143);transform-origin:0 0}
  .flyer{position:absolute;left:160px;width:1058px;height:620px;overflow:hidden;box-shadow:4px 6px 10px rgba(0,0,0,.28)}
  .flyer--front{top:48px;background:var(--paper)}
  .flyer--back{top:720px;height:622px;background:var(--mist)}
  .flyer svg.art{position:absolute;left:0;top:0}
  .brand{position:absolute;display:flex;align-items:center;gap:12px;font-weight:800;color:var(--ink);letter-spacing:-1px;white-space:nowrap;line-height:1}
  .brand__dot{width:20px;height:20px;border-radius:50%;background:var(--red);flex:none}
  .front .brand{left:95px;top:115px;font-size:54px}
  .headline{position:absolute;left:70px;top:366px;font-weight:700;line-height:1}
  .headline span{display:block}
  .headline .l1{color:var(--red);font-size:38px;margin-bottom:6px}
  .headline .l2{color:var(--green);font-size:43px;margin-bottom:6px}
  .headline .l3{color:var(--ink);font-size:43px;font-weight:600;margin-bottom:6px}
  .headline .l4{color:var(--teal);font-size:30px}
  .call{position:absolute;left:95px;top:566px;color:#fff;font-size:33px;font-weight:600}
  .web-front{position:absolute;left:740px;top:582px;color:#fff;font-size:27px;font-weight:700}
  .back .brand{left:770px;top:200px;font-size:42px}
  .section-title{position:absolute;left:80px;top:252px;font-size:26px;font-weight:700}
  .services{position:absolute;left:33px;top:293px;width:987px;height:114px;background:var(--green-band);list-style:none}
  .services li{position:absolute;display:flex;align-items:center;gap:12px;color:var(--ink);font-size:19px;font-weight:700;white-space:nowrap}
  .services svg{width:30px;height:30px}
  .expanding{position:absolute;left:78px;top:428px;line-height:1}
  .expanding .big{display:block;color:var(--red);font-size:52px;font-weight:700}
  .expanding .sub{display:block;font-size:29px;font-weight:700;margin-top:4px}
  .values{position:absolute;left:492px;top:430px;width:395px}
  .values h3{font-size:22px;font-weight:700;margin-bottom:8px}
  .values p{font-size:13px;line-height:1.2;font-weight:400}
  .footer{position:absolute;left:0;top:538px;width:1058px;height:64px;background:var(--ink);color:#fff;font-size:15px;font-weight:600}
  .footer .item{position:absolute;display:flex;align-items:flex-start;gap:10px;top:14px;line-height:1.15;white-space:nowrap}
  .footer svg{width:18px;height:18px;flex:none}
</style>
</head>
<body>
<div class="stage">

  <section class="flyer flyer--front front">
    <svg class="art" width="1058" height="620" viewBox="160 48 1058 620">
      <polygon points="160,148 160,270 410,352" fill="var(--green)"/>
      <polygon points="160,270 410,352 160,380" fill="var(--ink)"/>
      <g role="img" aria-label="Photo of smiling office team working at laptops">
        <polygon points="488,48 872,48 792,305 410,352" fill="var(--photo-warm)"/>
      </g>
      <g role="img" aria-label="Photo of call center agents wearing headsets">
        <polygon points="872,48 1218,48 1218,258 792,305" fill="var(--photo-cool)"/>
      </g>
      <line x1="872" y1="48" x2="790" y2="310" stroke="var(--teal)" stroke-width="4"/>
      <polygon points="410,352 1218,258 1218,372 420,356" fill="var(--red)"/>
      <polygon points="160,382 420,356 1218,372 1218,392 160,400" fill="#e6e6e6" opacity=".6"/>
      <g role="img" aria-label="Photo of smiling assistant with headset at a desk">
        <circle cx="788" cy="495" r="99" fill="var(--photo-cool)" stroke="var(--teal)" stroke-width="4"/>
      </g>
      <g role="img" aria-label="Photo of friendly assistant wearing a headset">
        <circle cx="1033" cy="495" r="99" fill="var(--photo-warm)" stroke="var(--teal)" stroke-width="4"/>
      </g>
      <polygon points="160,590 640,590 648,603 160,603" fill="#d8d8d8"/>
      <polygon points="160,603 648,603 665,668 160,668" fill="var(--teal)"/>
      <rect x="655" y="628" width="205" height="40" fill="var(--red)"/>
      <rect x="864" y="628" width="354" height="40" fill="var(--green)"/>
    </svg>
    <div class="brand"><span class="brand__dot"></span>BrimDesk</div>
    <h1 class="headline">
      <span class="l1">SOME CALL THEM</span>
      <span class="l2">SUPER HUMAN</span>
      <span class="l3">WE CALL THEM</span>
      <span class="l4">VIRTUAL ASSISTANTS!</span>
    </h1>
    <div class="call">CALL:(555) 014-2290</div>
    <div class="web-front">www.brimdesk.biz</div>
  </section>

  <section class="flyer flyer--back back">
    <svg class="art" width="1058" height="622" viewBox="160 720 1058 622">
      <rect x="160" y="720" width="1058" height="222" fill="var(--paper)"/>
      <g role="img" aria-label="Photo of a smiling man surrounded by floating video call windows">
        <polygon points="170,730 540,730 540,920 170,915" fill="#dde8ef"/>
      </g>
      <g role="img" aria-label="Photo of a smiling assistant with headset in front of a digital world map">
        <polygon points="592,720 1000,720 926,940 500,930" fill="var(--photo-cool)"/>
      </g>
      <line x1="592" y1="720" x2="500" y2="930" stroke="var(--green)" stroke-width="3"/>
      <polygon points="1000,720 1040,720 930,942" fill="var(--red)"/>
      <polygon points="160,918 922,942 160,942" fill="var(--teal)"/>
      <g role="img" aria-label="Photo of a businessman in a suit reading a tablet">
        <polygon points="1110,1085 1218,1085 1218,1342 1010,1342 1010,1300 1070,1190" fill="var(--photo-warm)"/>
      </g>
      <rect x="160" y="1324" width="645" height="18" fill="var(--red)"/>
      <rect x="810" y="1324" width="408" height="18" fill="var(--teal)"/>
    </svg>
    <div class="brand"><span class="brand__dot"></span>BrimDesk</div>
    <h2 class="section-title">OUR SERVICE</h2>
    <ul class="services">
      <li style="left:45px;top:12px"><svg viewBox="0 0 30 30"><rect x="7" y="4" width="16" height="22" fill="none" stroke="#fff" stroke-width="2"/><path d="M11 10h8M11 15h8M11 20h5" stroke="#fff" stroke-width="2"/></svg>VIRTUAL CONTENT</li>
      <li style="left:322px;top:12px"><svg viewBox="0 0 30 30"><rect x="3" y="5" width="18" height="14" fill="none" stroke="#fff" stroke-width="2"/><circle cx="20" cy="19" r="7" fill="none" stroke="#fff" stroke-width="2"/><path d="M13 19h14M20 12v14" stroke="#fff" stroke-width="1.5"/></svg>VIRTUAL ORGANIZATION</li>
      <li style="left:663px;top:12px"><svg viewBox="0 0 30 30"><rect x="2" y="7" width="26" height="17" fill="none" stroke="#fff" stroke-width="2"/><path d="M2 7l13 10 13-10" fill="none" stroke="#fff" stroke-width="2"/></svg>CLIENT MAILINGS</li>
      <li style="left:45px;top:68px"><svg viewBox="0 0 30 30"><rect x="3" y="6" width="24" height="21" fill="none" stroke="#fff" stroke-width="2"/><path d="M3 12h24M9 3v6M21 3v6M8 16h4M14 16h4M20 16h4M8 21h4M14 21h4" stroke="#fff" stroke-width="2"/></svg>EVENT PLANNING</li>
      <li style="left:320px;top:68px"><svg viewBox="0 0 30 30"><path d="M15 3a6 6 0 0 1 6 6c0 5-6 11-6 11S9 14 9 9a6 6 0 0 1 6-6z" fill="none" stroke="#fff" stroke-width="2"/><circle cx="15" cy="9" r="2" fill="#fff"/><path d="M3 27l5-8h4M27 27l-5-8h-4M3 27h24" fill="none" stroke="#fff" stroke-width="2"/></svg>TRAVEL ARRANGEMENTS</li>
    </ul>
    <div class="expanding"><span class="big">EXPANDING</span><span class="sub">BUSINESS VIRTUALLY</span></div>
    <div class="values">
      <h3>VALUES STATEMENT</h3>
      <p>We are committed to become your invaluable virtual resource by providing revolutionary, quality services to expand your business virtually and save your valuable time.</p>
    </div>
    <div class="footer">
      <div class="item" style="left:66px"><svg viewBox="0 0 18 18"><path d="M9 1a6 6 0 0 1 6 6c0 4-6 10-6 10S3 11 3 7a6 6 0 0 1 6-6z" fill="#fff"/><circle cx="9" cy="7" r="2" fill="var(--ink)"/></svg><span>P.O. BOX 408217 AUSTIN,<br>TEXAS 78701</span></div>
      <div class="item" style="left:305px"><svg viewBox="0 0 18 18"><rect x="5" y="1" width="9" height="16" rx="1.5" fill="none" stroke="#fff" stroke-width="1.5"/><circle cx="9.5" cy="14" r="1" fill="#fff"/></svg><span>(555) 014-2290</span></div>
      <div class="item" style="left:467px"><svg viewBox="0 0 18 18"><rect x="1" y="4" width="16" height="11" fill="#fff"/><path d="M1 4l8 6 8-6" fill="none" stroke="var(--ink)" stroke-width="1.5"/></svg><span>support@brimdesk.biz</span></div>
      <div class="item" style="left:690px"><svg viewBox="0 0 18 18"><rect x="1" y="3" width="16" height="11" fill="none" stroke="#fff" stroke-width="1.5"/><path d="M4 7h10M4 10h6M6 16h6" stroke="#fff" stroke-width="1.5"/></svg><span>www.brimdesk.biz</span></div>
    </div>
  </section>

</div>
</body>
</html>
```